Landing page for Brook Aerowing

Re-design the landing page for www.brookaerowing.example. It needs to be flatter and work with both PC, Mac and Mobile. Sites I like are as follows:
http://tarnelflight.example
http://qoskyway.example
http://www.velmoplanes.example
http://www.dunmorewing.example/dmw.php
http://www.ulvane.example
http://www.cedrolskies.example
http://www.pembrookflighthub.example
http://www.corvallowings.example
http://www.tessorivawings.example

We are a Marlow 48 Dealer, SkyNoble FBO member, Vortell Circle FBO, QMR Preferred FBO located only 6 miles from Downtown Atlanta. Providing Aircraft charter, Aircraft sales, Aircraft Maintenance, Aircraft Line Services and Hangar, and Parts Support.

Reason: I have six people reviewing designs within the company and will not be able to complete the review until next week.

Target Market(s)

Pilot's looking for a place to take care of them in Atlanta

Industry/Entity Type

Group

Colors
fbed22
0555a3

Requirements
Must have
• Slogan "Focused on Arrival" and "Sensational Southern Service"

```html
<!DOCTYPE html>
<html lang="en">
<head>
<meta charset="utf-8">
<title>Brook Aerowing – Focused on Arrival</title>
<link href="https://fonts.googleapis.com/css2?family=Open+Sans:wght@300;400;600;700&display=swap" rel="stylesheet">
<style>
:root{
  --yellow:#fbed22;
  --blue:#0555a3;
  --royal:#0a0ae6;
  --page:#f2f2f2;
  --white:#ffffff;
  --text:#666666;
  --dark:#222222;
  --footer-text:#333333;
}
*{margin:0;padding:0;box-sizing:border-box}
html,body{width:906px;height:1200px;overflow:hidden}
body{background:var(--page);font-family:'Open Sans',sans-serif;color:var(--text);position:relative}
.top-band{position:absolute;left:0;top:0;width:906px;height:94px;background:var(--white)}
.wrap{position:absolute;left:125px;width:656px}
.brand{position:absolute;left:125px;top:22px;display:flex;align-items:center;gap:7px;font-weight:700;font-size:19px;color:var(--blue)}
.brand .mark{width:16px;height:16px;background:var(--yellow);border-radius:50%}
.social{position:absolute;left:690px;top:13px;display:flex;gap:5px}
.social span{width:27px;height:27px;border-radius:50%;display:block}
.social .s1{background:#2fb1e0}.social .s2{background:#3b5998}.social .s3{background:#1a75bb}
.search{position:absolute;left:612px;top:52px;width:169px;height:19px;background:#ebebeb;font-size:8px;color:#555;padding:4px 7px}
.search svg{position:absolute;right:4px;top:2px}
.nav{top:78px;height:42px;display:flex;background:var(--yellow)}
.nav a{flex:1 1 auto;white-space:nowrap;font-size:8.4px;font-weight:600;color:var(--dark);text-decoration:none;display:flex;align-items:center;justify-content:center;padding:0 4px;border-right:1px solid #f3e21b}
.nav a.active{background:var(--royal);color:var(--white);padding:0 9px}
.nav a:last-child{border-right:none}
.hero{top:127px;height:242px;overflow:hidden}
.hero-photo{position:absolute;inset:0;background:linear-gradient(180deg,#8a8f96 0%,#5a6472 35%,#2d3b55 62%,#3a4152 80%,#c9ccd2 100%)}
.slogan{position:absolute;left:419px;top:81px;width:237px;height:76px;background:var(--royal);clip-path:polygon(22px 0,100% 0,100% 100%,0 100%);color:var(--white);text-align:center;padding-left:24px;padding-top:20px}
.slogan h2{font-size:19px;font-weight:700;line-height:1.1}
.slogan p{font-size:12px;font-weight:300}
.dots{position:absolute;right:9px;bottom:14px;display:flex;gap:3px}
.dots i{width:11px;height:11px;border-radius:50%;background:#000;display:block}
.dots i:first-child{background:var(--royal)}
.h-title{color:var(--royal);font-weight:400;font-size:18px;text-align:center}
.welcome{top:385px}
.welcome p{margin-top:12px;font-size:9.6px;font-weight:300;line-height:17.6px;text-align:center;color:#555}
.divider{height:30px;background:radial-gradient(ellipse at 50% 0,rgba(0,0,0,.12),rgba(0,0,0,0) 70%)}
.div1{top:497px}
.services-title{top:517px}
.cards{top:556px;display:flex;gap:13px}
.card{width:210px}
.card .ph{height:130px}
.card h3{color:var(--blue);font-size:10px;font-weight:700;line-height:17.6px;margin-top:13px}
.card p{font-size:10px;line-height:17.6px;margin-top:10px;color:#444;font-weight:300}
.div2{top:816px}
.view-more{position:absolute;left:386px;top:816px;width:135px;height:31px;background:var(--blue);clip-path:polygon(0 0,100% 0,90% 100%,10% 100%);color:var(--white);font-weight:700;font-size:12.5px;display:flex;align-items:center;justify-content:center}
.box{position:absolute;top:881px;height:197px;background:#fafafa;box-shadow:0 1px 3px rgba(0,0,0,.18)}
.box .inner{position:absolute;left:6px;right:6px;top:6px;bottom:6px;background:var(--white);border-top:1px solid #ddd}
.box h4{color:var(--blue);font-weight:400;font-size:13px;text-align:center;margin-top:10px}
.partners{left:125px;width:432px}
.ebook{left:571px;width:210px}
.ebook .inner{background:#fafafa}
.badge{position:absolute;display:block}
.cover{position:absolute;left:60px;top:40px;width:90px;height:134px;background:linear-gradient(180deg,#fff 0%,#eef 52%,#3a3f4a 58%,#151a22 100%);border:1px solid #ccc}
.footer{position:absolute;left:0;top:1104px;width:906px;height:96px;background:var(--white);text-align:center}
.footer .dealer{display:block;margin-top:20px;font-size:11px;font-weight:600;color:var(--footer-text)}
.footer p{font-size:9px;color:var(--footer-text);margin-top:14px}
</style>
</head>
<body>
<div class="top-band"></div>
<div class="brand"><span class="mark"></span>Brook Aerowing</div>
<div class="social" aria-label="Social links"><span class="s1"></span><span class="s2"></span><span class="s3"></span></div>
<div class="search">Search
  <svg width="14" height="14" viewBox="0 0 14 14"><circle cx="5.5" cy="5.5" r="4" fill="none" stroke="#333" stroke-width="1.6"/><line x1="8.5" y1="8.5" x2="13" y2="13" stroke="#333" stroke-width="2"/></svg>
</div>
<nav class="wrap nav">
  <a class="active">Home</a><a>About Us</a><a>Aircraft Management</a><a>Charter</a><a>FBO Services</a><a>Maintenance</a><a>Aircraft Parts</a><a>Aircraft</a><a>Sales</a><a>Resources</a><a>Contact Us</a>
</nav>
<section class="wrap hero">
  <div class="hero-photo" role="img" aria-label="Business jet parked on the ramp in front of the Brook Aerowing hangar at dusk"></div>
  <div class="slogan"><h2>Focused on Arrival</h2><p>Sensational Southern Service</p></div>
  <div class="dots"><i></i><i></i><i></i><i></i></div>
</section>
<section class="wrap welcome">
  <h1 class="h-title">Welcome to Brook Aerowing</h1>
  <p>Brook Aerowing offers a full range of aircraft management services.Take full advantage of aircraft ownership without worrying about the administrative and operational issues.&nbsp; Our professional staff will manage all aspects of the day to day operation of your aircraft. Let our management team provide you with professional flight services individually structured to meet your needs.</p>
</section>
<div class="wrap divider div1"></div>
<h2 class="wrap h-title services-title">Our Services</h2>
<section class="wrap cards">
  <div class="card"><div class="ph" role="img" aria-label="Smiling charter flight crew in uniform" style="background:linear-gradient(135deg,#dfe6ee,#6b7ea6 55%,#1d2a4f)"></div><h3>Aircraft Charter</h3><p>Payroll, drug screening, uniforms, background checks</p></div>
  <div class="card" style="margin-left:-1px"><div class="ph" role="img" aria-label="Pilots at the controls in a jet cockpit" style="background:linear-gradient(180deg,#6d6f73,#c9ccd1 45%,#2b2d31)"></div><h3>Block time and custom innovative ownershipprograms</h3><p>Training exceeds FAA requirements, simulator training with Aerotrain Academy</p></div>
  <div class="card" style="margin-left:2px"><div class="ph" role="img" aria-label="Passengers and crew standing beside a private jet" style="background:linear-gradient(135deg,#e6e8eb,#8a93a3 50%,#1f2d55)"></div><h3>Line Services</h3><p style="margin-top:6px">Training exceeds FAA requirements, simulator training with Aerotrain Academy</p></div>
</section>
<div class="wrap divider div2"></div>
<div class="view-more">View More</div>
<section class="box partners">
  <div class="inner">
    <h4>Our logos</h4>
    <svg class="badge" style="left:30px;top:45px" width="140" height="70" viewBox="0 0 140 70" role="img" aria-label="50th anniversary badge"><path d="M5 45 L130 10 L138 30 L12 64 Z" fill="#5aa0d8"/></svg>
    <svg class="badge" style="left:188px;top:80px" width="118" height="28" role="img" aria-label="Safety audit rating badge"><rect x="1" y="1" width="116" height="26" fill="#fff" stroke="#333"/><rect x="3" y="3" width="72" height="22" fill="#2b4a8b"/></svg>
    <svg class="badge" style="left:320px;top:58px" width="64" height="52" role="img" aria-label="Safety program badge"><rect x="4" y="10" width="56" height="36" rx="4" fill="#3a9a3a"/></svg>
    <svg class="badge" style="left:30px;top:128px" width="360" height="20" role="img" aria-label="Partner and membership badges">
      <rect x="0" y="7" width="40" height="6" fill="#888"/><circle cx="57" cy="10" r="7" fill="#1e3a8a"/><rect x="70" y="3" width="36" height="14" fill="#1e4aa8"/><rect x="130" y="3" width="64" height="14" fill="#222"/><rect x="210" y="3" width="44" height="14" fill="#f2c500"/><rect x="270" y="3" width="14" height="14" fill="#555"/><rect x="300" y="3" width="52" height="14" fill="#1e2f7a"/>
    </svg>
  </div>
</section>
<section class="box ebook">
  <div class="inner">
    <h4 style="margin-top:4px">Download Our E-Book</h4>
    <div class="cover" role="img" aria-label="E-book cover showing the FBO ramp and line service details"></div>
  </div>
</section>
<footer class="footer">
  <span class="dealer">Marlow 48</span>
  <p>©Copyright 2007Brook Aerowing &amp; Leasing All Rights Reserved</p>
</footer>
</body>
</html>
```